GATHERING MARIGOLDS

ID LIKE TO CREATE A HARD COPY BOOK COVER AND AN EBOOK COVER : ID LIKE TO INCORPORATE A FACE WITH A WEDDING VEIL THAT UNCOVERS THE FACE OF THE SUBJECT NARCISSISM

```html
<!DOCTYPE html>
<html lang="en">
<head>
<meta charset="utf-8">
<title>Gathering Marigolds – Book Cover</title>
<link rel="stylesheet" href="https://fonts.googleapis.com/css2?family=Italiana&family=Cormorant+Garamond:wght@500&family=Tinos&display=swap">
<style>
  :root {
    --paper: #f1f1f1;
    --paper-deep: #e4e4e4;
    --veil-white: #fbfbfb;
    --skin-light: #f1ddd0;
    --skin-warm: #e2bfa9;
    --skin-shadow: #cfa48c;
    --hair-gold: #d8bfa0;
    --hair-deep: #b99a7a;
    --title-red: #b0161e;
    --ink: #1d1d1d;
  }
  html, body {
    margin: 0;
    padding: 0;
    overflow: hidden;
    background: #ffffff;
  }
  .cover {
    position: relative;
    width: 1200px;
    height: 815px;
    overflow: hidden;
    background: linear-gradient(180deg, var(--paper) 0%, var(--paper-deep) 100%);
  }
  .back-veil {
    position: absolute;
    left: 420px;
    top: 0;
    width: 210px;
    height: 815px;
    background: linear-gradient(90deg, rgba(255,255,255,0) 0%, rgba(255,255,255,0.8) 60%, var(--veil-white) 100%);
  }
  .front-photo {
    position: absolute;
    left: 624px;
    top: 0;
    width: 576px;
    height: 815px;
    background:
      linear-gradient(115deg, rgba(255,255,255,0.75) 0%, rgba(255,255,255,0) 22%, rgba(255,255,255,0) 30%, rgba(255,255,255,0.55) 38%, rgba(255,255,255,0) 48%),
      radial-gradient(ellipse 150px 250px at 385px 300px, var(--skin-light) 0%, rgba(241,221,208,0.9) 50%, rgba(241,221,208,0) 100%),
      radial-gradient(ellipse 190px 300px at 410px 330px, var(--skin-warm) 0%, rgba(226,191,169,0.6) 55%, rgba(226,191,169,0) 100%),
      radial-gradient(ellipse 90px 330px at 545px 360px, var(--hair-deep) 0%, rgba(185,154,122,0.55) 50%, rgba(185,154,122,0) 100%),
      radial-gradient(ellipse 200px 420px at 500px 330px, var(--hair-gold) 0%, rgba(216,191,160,0.5) 55%, rgba(216,191,160,0) 100%),
      radial-gradient(ellipse 120px 120px at 330px 470px, var(--skin-shadow) 0%, rgba(207,164,140,0) 100%),
      linear-gradient(90deg, var(--veil-white) 0%, #f6f6f6 45%, #ece6e2 100%);
  }
  .front-veil-edge {
    position: absolute;
    left: 624px;
    top: 0;
    width: 576px;
    height: 815px;
    background:
      linear-gradient(200deg, rgba(255,255,255,0) 55%, rgba(255,255,255,0.85) 72%, rgba(255,255,255,0) 82%),
      linear-gradient(90deg, rgba(255,255,255,0.9) 0%, rgba(255,255,255,0) 30%);
  }
  .back-copy {
    position: absolute;
    left: 84px;
    top: 114px;
    width: 420px;
    font-family: "Tinos", serif;
    font-size: 14px;
    line-height: 18.9px;
    color: var(--ink);
    text-align: justify;
    text-align-last: center;
    hyphens: auto;
  }
  .back-copy p { margin: 0; }
  .back-copy .gap { margin-top: 18.9px; }
  .spine-title, .spine-author {
    position: absolute;
    writing-mode: vertical-rl;
    margin: 0;
    white-space: nowrap;
  }
  .spine-title {
    left: 592px;
    top: 54px;
    font-family: "Italiana", serif;
    font-size: 33px;
    font-weight: 400;
    color: var(--title-red);
  }
  .spine-author {
    left: 587px;
    top: 522px;
    font-family: "Cormorant Garamond", serif;
    font-weight: 500;
    font-size: 22px;
    letter-spacing: 0.32em;
    color: var(--ink);
  }
  .front-title {
    position: absolute;
    left: 650px;
    width: 560px;
    top: 548px;
    margin: 0;
    text-align: center;
    font-family: "Italiana", serif;
    font-weight: 400;
    font-size: 82px;
    line-height: 76px;
    color: var(--title-red);
  }
  .front-author {
    position: absolute;
    left: 660px;
    width: 520px;
    top: 743px;
    margin: 0;
    text-align: center;
    font-family: "Cormorant Garamond", serif;
    font-weight: 500;
    font-size: 25px;
    letter-spacing: 0.3em;
    color: var(--ink);
  }
</style>
</head>
<body>
  <main class="cover">
    <div class="back-veil" role="img" aria-label="Sheer white wedding veil drifting across the spine"></div>
    <div class="front-photo" role="img" aria-label="Photograph of a blonde woman's face partly uncovered by a sheer white wedding veil"></div>
    <div class="front-veil-edge"></div>

    <section class="back-copy">
      <p>Lorem ipsum dolor sit amet, consectetur adipiscing elit, sed do eiusmod tempor incididunt ut labore et dolore magna aliqua. Quis ipsum suspendisse ultrices gravida. Risus commodo viverra maecenas accumsan lacus vel facilisis.</p>
      <p class="gap">Lorem ipsum dolor sit amet, consectetur adipiscing elit, sed do eiusmod tempor incididunt ut labore et dolore magna aliqua. Quis ipsum suspendisse ultrices gravida. Risus commodo viverra maecenas accumsan lacus vel facilisis.</p>
      <p>Lorem ipsum dolor sit amet, consectetur adipiscing elit, sed do eiusmod tempor incididunt ut labore et dolore magna aliqua. Quis ipsum suspendisse ultrices gravida. Risus commodo viverra maecenas accumsan lacus vel facilisis. Lorem ipsum dolor sit amet, consectetur adipiscing elit, sed do eiusmod tempor incididunt ut labore et dolore magna aliqua. Quis ipsum suspendisse ultrices graa maecenas accumsan lacus vel facilisis.</p>
      <p class="gap">Lorem ipsum dolor sit amet, consectetur adipiscing elit, sed do eiusmod tempor incididunt ut labore et. Quis ipsum suspendisse ultrices gravida. Risus commodo viverra maecenas accumsan lacus vel facilisis.</p>
      <p>Consectetur adipiscing elit, sed do eiusmod tempor incididunt ut labore et dolore magna aliqua. Quis ipsum suspendisse ultrices gravida. Risus commodo viverra maecenas accumsan lacus vel facilisis.</p>
    </section>

    <h2 class="spine-title">GATHERING MARIGOLDS</h2>
    <p class="spine-author">AUTHOR NAME</p>

    <h1 class="front-title">GATHERING<br>MARIGOLDS</h1>
    <p class="front-author">AUTHOR NAME</p>
  </main>
</body>
</html>
```